FinTech company looking to revamp and expand client-facing interface for our financial models

Halvern Quotient currently has a very simple website that allows clients to interact with our financial models. We are looking to completely redesign the current site and add several extra pages to provide extra functionality. We want the design to have a modern, slick feel, that will work on both a desktop or a tablet. It should be straightforward for clients to move between different pages at any time, and clear from the layout how to interact with the more advanced features. We have included screenshots of existing pages in the attached design brief, as well as sketches of the functionality required by the new pages, but can't provide a direct link to the current site.
Target Market(s)
Professional investors that will be paying to access the interface
Industry/Entity Type
Finance
Number of Pages Required
4 page
Colors
Designer to choose colors to be used in the design.
Look and feel
Each slider illustrates characteristics of the customer's brand and the style your logo design should communicate.

```html
<!DOCTYPE html>
<html lang="en">
<head>
<meta charset="utf-8">
<title>Halvern Quotient – Models</title>
<link href="https://fonts.googleapis.com/css2?family=Roboto:wght@400;500;700&display=swap" rel="stylesheet">
<style>
:root{
  --canvas:#d9d9d9;
  --bar:#474a6a;
  --search:#5c5f80;
  --white:#ffffff;
  --page:#f4f4f4;
  --panel-head:#efefef;
  --teal:#5fd0be;
  --link:#4a9fe0;
  --ink:#333333;
  --muted:#8a8a8a;
  --line:#e2e2e2;
  --alert:#e0404a;
}
*{box-sizing:border-box;margin:0;padding:0}
html,body{width:1200px;height:881px;overflow:hidden}
body{background:var(--canvas);font-family:'Roboto',sans-serif;color:var(--ink);position:relative}
.screen{position:absolute;width:900px;background:var(--page);transform-origin:0 0;box-shadow:0 6px 18px rgba(0,0,0,.18);overflow:hidden}
.screen--models{left:45px;top:48px;height:728px;transform:scale(.5333)}
.screen--factors{left:45px;top:478px;height:664px;transform:scale(.5333)}
.screen--wide{left:610px;top:67px;height:543px;transform:scale(.5767)}
.topbar{height:42px;background:var(--bar);display:flex;align-items:center;padding:0 34px 0 42px;color:var(--white)}
.brand{font-weight:700;font-size:14px;letter-spacing:.2px}
.search{margin-left:26px;width:160px;height:26px;border-radius:13px;background:var(--search);display:flex;align-items:center;justify-content:space-between;padding:0 12px;font-size:10px}
.tools{margin-left:auto;display:flex;align-items:center;gap:14px;font-size:10px}
.bell{width:22px;height:22px;border-radius:50%;background:var(--search);display:flex;align-items:center;justify-content:center;position:relative}
.bell::after{content:"";position:absolute;top:2px;right:3px;width:6px;height:6px;border-radius:50%;background:var(--alert)}
.expand{width:22px;height:22px;display:flex;align-items:center;justify-content:center}
.avatar{width:24px;height:24px;border-radius:50%;background:linear-gradient(#c9a58a,#7a6a5e);border:2px solid var(--white)}
.user{margin-left:-8px}
.nav{height:40px;background:var(--white);border-bottom:1px solid var(--line);display:flex;align-items:center;gap:32px;padding-left:42px;font-size:13px;color:var(--muted)}
.nav a{display:flex;align-items:center;gap:6px;text-decoration:none;color:var(--muted)}
.nav a.is-active{color:var(--link)}
.page-title{font-size:13px;font-weight:400;margin:18px 0 0 41px}
.panel{margin:12px 34px 0 42px;background:var(--white);box-shadow:0 0 3px rgba(0,0,0,.05);overflow:hidden}
.panel--models{height:550px}
.panel--factors{height:484px}
.panel-head{height:43px;background:var(--panel-head);display:flex;align-items:stretch;padding-left:31px}
.panel-title{font-size:16px;font-weight:500;display:flex;align-items:center;width:99px}
.tab{display:flex;align-items:center;padding:0 12px;font-size:13px;margin-right:10px}
.tab.is-active{background:var(--white);border:1px solid var(--line);border-bottom:none}
.panel-body{padding:11px 31px 0 32px}
.filter{display:flex;align-items:center;height:36px}
.filter-key{width:61px;font-size:7px;font-weight:700}
.filter-label{font-size:11.5px;font-weight:500;margin-right:6px}
.filter input{width:113px;height:22px;border:1px solid var(--line);font:9px 'Roboto',sans-serif;color:var(--muted);padding-left:7px}
.export{display:flex;align-items:center;gap:7px;color:var(--link);font-size:14px;height:17px;margin:12px 0 13px}
table{border-collapse:collapse;table-layout:fixed;width:762px}
th{background:var(--teal);color:var(--white);font-weight:500;font-size:12px;height:35px;text-align:left;padding-left:9px;white-space:nowrap}
td{border:1px solid var(--line);font-size:9.5px;color:var(--muted);padding:0 6px;line-height:1.75}
.rows-tall td{height:61px}
.rows-short td{height:49px;padding-left:10px}
.nowrap{white-space:nowrap}
.footer{position:absolute;bottom:14px;left:0;right:0;text-align:center;font-size:10.5px;color:#555}
</style>
</head>
<body>

<section class="screen screen--models">
  <header class="topbar">
    <span class="brand">Halvern Quotient</span>
    <div class="search">Search<svg width="10" height="10" viewBox="0 0 10 10"><circle cx="4" cy="4" r="3" fill="none" stroke="#fff" stroke-width="1.5"/><line x1="6.2" y1="6.2" x2="9" y2="9" stroke="#fff" stroke-width="1.5"/></svg></div>
    <div class="tools">
      <span class="bell"><svg width="10" height="11" viewBox="0 0 10 11"><path d="M5 1a3 3 0 0 1 3 3v3l1 1.5H1L2 7V4a3 3 0 0 1 3-3z" fill="#fff"/><circle cx="5" cy="10" r="1" fill="#fff"/></svg></span>
      <span class="expand"><svg width="12" height="12" viewBox="0 0 12 12" fill="none" stroke="#fff" stroke-width="1.3"><path d="M1 4V1h3M8 1h3v3M11 8v3H8M4 11H1V8"/></svg></span>
      <span class="avatar" role="img" aria-label="User profile photo"></span>
      <span class="user">Mara Lind ⌄</span>
    </div>
  </header>
  <nav class="nav">
    <a class="is-active" href="#"><svg width="12" height="11" viewBox="0 0 12 11"><path d="M6 0l6 5h-2v6H7V7H5v4H2V5H0z" fill="currentColor"/></svg>Models</a>
    <a href="#"><svg width="11" height="11" viewBox="0 0 11 11"><circle cx="5.5" cy="5.5" r="3.5" fill="none" stroke="currentColor" stroke-width="2.4" stroke-dasharray="2 1.5"/></svg>Sensitivities</a>
    <a href="#"><svg width="12" height="11" viewBox="0 0 12 11"><path d="M6 0l1.8 3.7 4 .5-3 2.8.8 4L6 9 2.4 11l.8-4-3-2.8 4-.5z" fill="currentColor"/></svg>Favourites</a>
  </nav>
  <h2 class="page-title">Models</h2>
  <div class="panel panel--models">
    <div class="panel-head">
      <span class="panel-title">QVANE</span>
      <span class="tab is-active">250D</span><span class="tab">83D</span><span class="tab">42D</span>
    </div>
    <div class="panel-body">
      <div class="filter"><span class="filter-key">Quality</span><span class="filter-label">Threshold</span><input value="-10"></div>
      <div class="filter"><span class="filter-key">Abs. Stat</span><span class="filter-label">Threshold</span><input value="-10"></div>
      <div class="export"><svg width="14" height="12" viewBox="0 0 14 12" fill="none" stroke="currentColor" stroke-width="1.5"><path d="M7 2H1v9h10V7"/><path d="M6 7l6-6M8 1h4v4"/></svg>Export</div>
      <table class="rows-tall">
        <colgroup><col style="width:52px"><col style="width:75px"><col style="width:78px"><col style="width:65px"><col style="width:66px"><col style="width:66px"><col style="width:65px"><col style="width:60px"><col style="width:60px"><col style="width:59px"><col style="width:60px"><col style="width:56px"></colgroup>
        <thead><tr><th>ID ▾</th><th>Sector</th><th>Time</th><th>Quality</th><th>Stat 1</th><th>Stat 2</th><th>Stat 3</th><th>Stat 4</th><th>Stat 5</th><th>Stat 6</th><th>Stat 7</th><th>Stat 8</th></tr></thead>
        <tbody>
          <tr><td class="nowrap">Model 1</td><td>Materials</td><td>2019-07-03 12:15:00.000</td><td>30.2288</td><td>2.01574</td><td>23.305</td><td>-0.149368</td><td>22.3054</td><td>4.63714</td><td>0.945706</td><td>2.81949</td><td>2.60858</td></tr>
          <tr><td class="nowrap">Model 2</td><td>Industrials</td><td>2019-07-03 12:15:00.000</td><td>32.8694</td><td>0.87307</td><td>32.185</td><td>-0.0336927</td><td>33.9911</td><td>11.5693</td><td>-0.472968</td><td>-0.830458</td><td>6.80646</td></tr>
          <tr><td class="nowrap">Model 3</td><td>Consumer Discretionary</td><td>2019-07-03 12:15:00.000</td><td>1.66002</td><td>-0.569222</td><td>159.814</td><td>0.0252328</td><td>172.616</td><td>10.2875</td><td>-0.750396</td><td>-0.385309</td><td>4.69146</td></tr>
          <tr><td class="nowrap">Model 4</td><td>Information Technology</td><td>2019-07-03 12:15:00.000</td><td>45.6856</td><td>0.412148</td><td>202.488</td><td>0.00849232</td><td>205.834</td><td>11.9094</td><td>-0.137913</td><td>0.449595</td><td>3.85106</td></tr>
          <tr><td class="nowrap">Model 5</td><td>Information Technology</td><td>2019-07-03 12:15:00.000</td><td>75.7733</td><td>7.06728</td><td>188.605</td><td>0.016913</td><td>181.665</td><td>3.82241</td><td>0.981019</td><td>1.29847</td><td>3.34927</td></tr>
        </tbody>
      </table>
    </div>
  </div>
  <p class="footer">Copyright © 2019. All Rights Reserved.</p>
</section>

<section class="screen screen--factors">
  <header class="topbar">
    <span class="brand">Halvern Quotient</span>
    <div class="search">Search<svg width="10" height="10" viewBox="0 0 10 10"><circle cx="4" cy="4" r="3" fill="none" stroke="#fff" stroke-width="1.5"/><line x1="6.2" y1="6.2" x2="9" y2="9" stroke="#fff" stroke-width="1.5"/></svg></div>
    <div class="tools">
      <span class="bell"><svg width="10" height="11" viewBox="0 0 10 11"><path d="M5 1a3 3 0 0 1 3 3v3l1 1.5H1L2 7V4a3 3 0 0 1 3-3z" fill="#fff"/><circle cx="5" cy="10" r="1" fill="#fff"/></svg></span>
      <span class="expand"><svg width="12" height="12" viewBox="0 0 12 12" fill="none" stroke="#fff" stroke-width="1.3"><path d="M1 4V1h3M8 1h3v3M11 8v3H8M4 11H1V8"/></svg></span>
      <span class="avatar" role="img" aria-label="User profile photo"></span>
      <span class="user">Mara Lind ⌄</span>
    </div>
  </header>
  <nav class="nav">
    <a class="is-active" href="#"><svg width="12" height="11" viewBox="0 0 12 11"><path d="M6 0l6 5h-2v6H7V7H5v4H2V5H0z" fill="currentColor"/></svg>Models</a>
    <a href="#"><svg width="11" height="11" viewBox="0 0 11 11"><circle cx="5.5" cy="5.5" r="3.5" fill="none" stroke="currentColor" stroke-width="2.4" stroke-dasharray="2 1.5"/></svg>Sensitivities</a>
    <a href="#"><svg width="12" height="11" viewBox="0 0 12 11"><path d="M6 0l1.8 3.7 4 .5-3 2.8.8 4L6 9 2.4 11l.8-4-3-2.8 4-.5z" fill="currentColor"/></svg>Favourites</a>
  </nav>
  <h2 class="page-title">Models</h2>
  <div class="panel panel--factors">
    <div class="panel-head">
      <span class="panel-title">Factors</span>
      <span class="tab is-active">250D</span><span class="tab">83D</span><span class="tab">42D</span>
    </div>
    <div class="panel-body">
      <div class="filter"><span class="filter-key">Stat 1</span><span class="filter-label">Threshold</span><input value="-10"></div>
      <div class="filter"><span class="filter-key">Stat 2</span><span class="filter-label">Threshold</span><input value="-10"></div>
      <div class="filter"><span class="filter-key">Stat 3</span><span class="filter-label">Threshold</span><input value="-10"></div>
      <div class="export"><svg width="14" height="12" viewBox="0 0 14 12" fill="none" stroke="currentColor" stroke-width="1.5"><path d="M7 2H1v9h10V7"/><path d="M6 7l6-6M8 1h4v4"/></svg>Export</div>
      <table class="rows-short">
        <colgroup><col style="width:87px"><col style="width:95px"><col style="width:106px"><col style="width:83px"><col style="width:81px"><col style="width:78px"><col style="width:77px"><col style="width:81px"><col style="width:74px"></colgroup>
        <thead><tr><th style="padding-left:14px">Factor</th><th style="padding-left:34px">ID ▾</th><th style="padding-left:28px">Sector</th><th style="padding-left:21px">Stat 1</th><th style="padding-left:16px">Stat 2</th><th style="padding-left:17px">Stat 3</th><th style="padding-left:17px">Stat 4</th><th style="padding-left:19px">Stat 5</th><th style="padding-left:17px">Stat 6</th></tr></thead>
        <tbody>
          <tr><td>Factor 1</td><td style="padding-left:29px">Model 1</td><td style="padding-left:25px">Materials</td><td style="padding-left:23px">-1.4</td><td style="padding-left:22px">0.1</td><td style="padding-left:15px">-3.1</td><td style="padding-left:25px">0.7</td><td style="padding-left:25px">30.2</td><td style="padding-left:23px">0.9</td></tr>
          <tr><td>Factor 2</td><td style="padding-left:29px">Model 2</td><td style="padding-left:25px">Materials</td><td style="padding-left:23px">2.8</td><td style="padding-left:22px">0.1</td><td style="padding-left:15px">6.1</td><td style="padding-left:25px">100</td><td style="padding-left:25px">30.2</td><td style="padding-left:23px">0.9</td></tr>
          <tr><td>Factor 3</td><td style="padding-left:29px">Model 3</td><td style="padding-left:25px">Materials</td><td style="padding-left:23px">-3.7</td><td style="padding-left:22px">2.7</td><td style="padding-left:15px">-7.2</td><td style="padding-left:25px">100</td><td style="padding-left:25px">30.2</td><td style="padding-left:23px">0.9</td></tr>
          <tr><td>Factor 1</td><td style="padding-left:29px">Model 4</td><td style="padding-left:25px">Industrials</td><td style="padding-left:23px">2.8</td><td style="padding-left:22px">0.2</td><td style="padding-left:15px">2.7</td><td style="padding-left:25px">0.5</td><td style="padding-left:25px">32.9</td><td style="padding-left:23px">-0.5</td></tr>
          <tr><td>Factor 2</td><td style="padding-left:29px">Model 5</td><td style="padding-left:25px">Industrials</td><td style="padding-left:23px">0.8</td><td style="padding-left:22px">0.3</td><td style="padding-left:15px">2.5</td><td style="padding-left:25px">0.5</td><td style="padding-left:25px">32.9</td><td style="padding-left:23px">-0.5</td></tr>
        </tbody>
      </table>
    </div>
  </div>
  <p class="footer">Copyright © 2019. All Rights Reserved.</p>
</section>

<section class="screen screen--wide">
  <header class="topbar">
    <span class="brand">Halvern Quotient</span>
    <div class="search">Search<svg width="10" height="10" viewBox="0 0 10 10"><circle cx="4" cy="4" r="3" fill="none" stroke="#fff" stroke-width="1.5"/><line x1="6.2" y1="6.2" x2="9" y2="9" stroke="#fff" stroke-width="1.5"/></svg></div>
    <div class="tools">
      <span class="bell"><svg width="10" height="11" viewBox="0 0 10 11"><path d="M5 1a3 3 0 0 1 3 3v3l1 1.5H1L2 7V4a3 3 0 0 1 3-3z" fill="#fff"/><circle cx="5" cy="10" r="1" fill="#fff"/></svg></span>
      <span class="expand"><svg width="12" height="12" viewBox="0 0 12 12" fill="none" stroke="#fff" stroke-width="1.3"><path d="M1 4V1h3M8 1h3v3M11 8v3H8M4 11H1V8"/></svg></span>
      <span class="avatar" role="img" aria-label="User profile photo"></span>
      <span class="user">Mara Lind ⌄</span>
    </div>
  </header>
  <nav class="nav">
    <a class="is-active" href="#"><svg width="12" height="11" viewBox="0 0 12 11"><path d="M6 0l6 5h-2v6H7V7H5v4H2V5H0z" fill="currentColor"/></svg>Models</a>
    <a href="#"><svg width="11" height="11" viewBox="0 0 11 11"><circle cx="5.5" cy="5.5" r="3.5" fill="none" stroke="currentColor" stroke-width="2.4" stroke-dasharray="2 1.5"/></svg>Sensitivities</a>
    <a href="#"><svg width="12" height="11" viewBox="0 0 12 11"><path d="M6 0l1.8 3.7 4 .5-3 2.8.8 4L6 9 2.4 11l.8-4-3-2.8 4-.5z" fill="currentColor"/></svg>Favourites</a>
  </nav>
  <h2 class="page-title">Models</h2>
  <div class="panel panel--factors">
    <div class="panel-head">
      <span class="panel-title">Factors</span>
      <span class="tab is-active">250D</span><span class="tab">83D</span><span class="tab">42D</span>
    </div>
    <div class="panel-body">
      <div class="filter"><span class="filter-key">Stat 1</span><span class="filter-label">Threshold</span><input value="-10"></div>
      <div class="filter"><span class="filter-key">Stat 2</span><span class="filter-label">Threshold</span><input value="-10"></div>
      <div class="filter"><span class="filter-key">Stat 3</span><span class="filter-label">Threshold</span><input value="-10"></div>
      <div class="export"><svg width="14" height="12" viewBox="0 0 14 12" fill="none" stroke="currentColor" stroke-width="1.5"><path d="M7 2H1v9h10V7"/><path d="M6 7l6-6M8 1h4v4"/></svg>Export</div>
      <table class="rows-short">
        <colgroup><col style="width:87px"><col style="width:95px"><col style="width:106px"><col style="width:83px"><col style="width:81px"><col style="width:78px"><col style="width:77px"><col style="width:81px"><col style="width:74px"></colgroup>
        <thead><tr><th style="padding-left:14px">Factor</th><th style="padding-left:34px">ID ▾</th><th style="padding-left:28px">Sector</th><th style="padding-left:21px">Stat 1</th><th style="padding-left:16px">Stat 2</th><th style="padding-left:17px">Stat 3</th><th style="padding-left:17px">Stat 4</th><th style="padding-left:19px">Stat 5</th><th style="padding-left:17px">Stat 6</th></tr></thead>
        <tbody>
          <tr><td>Factor 1</td><td style="padding-left:29px">Model 1</td><td style="padding-left:25px">Materials</td><td style="padding-left:23px">-1.4</td><td style="padding-left:22px">0.1</td><td style="padding-left:15px">-3.1</td><td style="padding-left:25px">0.7</td><td style="padding-left:25px">30.2</td><td style="padding-left:23px">0.9</td></tr>
          <tr><td>Factor 2</td><td style="padding-left:29px">Model 2</td><td style="padding-left:25px">Materials</td><td style="padding-left:23px">2.8</td><td style="padding-left:22px">0.1</td><td style="padding-left:15px">6.1</td><td style="padding-left:25px">100</td><td style="padding-left:25px">30.2</td><td style="padding-left:23px">0.9</td></tr>
          <tr><td>Factor 3</td><td style="padding-left:29px">Model 3</td><td style="padding-left:25px">Materials</td><td style="padding-left:23px">-3.7</td><td style="padding-left:22px">2.7</td><td style="padding-left:15px">-7.2</td><td style="padding-left:25px">100</td><td style="padding-left:25px">30.2</td><td style="padding-left:23px">0.9</td></tr>
          <tr><td>Factor 1</td><td style="padding-left:29px">Model 4</td><td style="padding-left:25px">Industrials</td><td style="padding-left:23px">2.8</td><td style="padding-left:22px">0.2</td><td style="padding-left:15px">2.7</td><td style="padding-left:25px">0.5</td><td style="padding-left:25px">32.9</td><td style="padding-left:23px">-0.5</td></tr>
        </tbody>
      </table>
    </div>
  </div>
</section>

</body>
</html>
```